Resposive web site in 4 languages + image gallery + logo design

We need a web page, which will work on all devices.
I have uploaded web page concept.
Company name: Valqueno
Industry/Entity Type
It Company
Logo Text
quality matters
Coding
Coded - Design and coding required
Number of Pages Required
1 page

```html
<!DOCTYPE html>
<html lang="en">
<head>
<meta charset="utf-8">
<title>Valqueno – Woodworks, Stoneworks, Restoration</title>
<link rel="stylesheet" href="https://fonts.googleapis.com/css2?family=Raleway:wght@300;400;600;700;800&family=Open+Sans:wght@400;600&display=swap">
<style>
:root{
  --ink:#333a48;
  --text:#555a63;
  --accent:#1f9ae0;
  --dark:#1c1a18;
  --band:#2a2623;
  --footer:#4a4d55;
  --line:#d9dbe0;
  --white:#ffffff;
}
*{box-sizing:border-box;margin:0;padding:0}
html,body{width:1200px;height:2995px;overflow:hidden}
body{position:relative;background:var(--white);font-family:"Open Sans",Arial,sans-serif;color:var(--text)}
.abs{position:absolute}

/* hero */
.hero{left:0;top:0;width:1200px;height:566px;background:radial-gradient(ellipse at 40% 30%,#4a3b30 0%,#2a221d 45%,#141210 100%)}
.brand{display:flex;align-items:center;gap:14px;font-family:"Raleway",Arial,sans-serif;font-weight:600;font-size:36px}
.brand .dot{width:30px;height:30px;border-radius:50%;background:var(--accent)}
.hero .brand{left:100px;top:34px;color:var(--white)}
.nav{right:100px;top:48px;display:flex;gap:60px;font-family:"Raleway",Arial,sans-serif;font-weight:700;font-size:12px;color:var(--white);letter-spacing:.3px}
.nav .lang{display:flex;align-items:center;gap:8px}
.nav .flag{width:16px;height:10px;background:linear-gradient(#c8102e 0 33%,#1d3f8a 33% 66%,#fff 66%)}
.hero-title{left:0;width:1200px;top:238px;text-align:center;font-family:"Raleway",Arial,sans-serif;font-weight:800;font-size:42px;color:var(--white);letter-spacing:1px}
.hero-sub{left:0;width:1200px;top:296px;text-align:center;font-family:"Raleway",Arial,sans-serif;font-weight:400;font-size:29px;color:var(--white)}
.btn{background:var(--accent);color:var(--white);font-family:"Raleway",Arial,sans-serif;font-weight:700;font-size:12px;display:flex;align-items:center;justify-content:center;border-radius:2px}
.hero .btn{left:520px;top:362px;width:160px;height:40px}
.dots{left:1160px;top:226px;display:flex;flex-direction:column;gap:17px}
.dots span{width:9px;height:9px;border-radius:50%;background:#6b625b}

/* services */
.section-title{left:0;width:1200px;text-align:center;font-family:"Raleway",Arial,sans-serif;font-weight:700;font-size:31px;color:var(--ink)}
.photo{position:absolute}
.service h3{font-family:"Raleway",Arial,sans-serif;font-weight:300;font-size:32px;color:var(--ink);margin-bottom:16px}
.service p{font-size:12.5px;line-height:26px;color:var(--text)}
.ticks{display:grid;grid-template-columns:140px 160px;row-gap:8px;margin-top:20px;font-size:13px;color:var(--text);list-style:none}
.ticks li{display:flex;align-items:center;gap:12px}
.ticks svg{width:11px;height:9px}

/* about */
.about{left:0;top:1888px;width:1200px;height:488px;background:radial-gradient(ellipse at 30% 50%,#3a322b 0%,#211d1a 70%)}
.about h2{left:100px;top:88px;font-family:"Raleway",Arial,sans-serif;font-weight:700;font-size:30px;color:var(--white)}
.about .copy{left:100px;top:146px;width:450px;font-size:12.5px;line-height:22px;color:#eee}
.about .copy p{margin-bottom:22px}
.about .sign{color:var(--accent);font-weight:600}

/* contact */
.contact-sub{left:0;width:1200px;top:2488px;text-align:center;font-family:"Raleway",Arial,sans-serif;font-size:14px;color:var(--text);letter-spacing:.3px}
.contact-brand{left:166px;top:2574px;color:var(--ink)}
.contact-brand .dot{width:34px;height:34px}
.contact-list{left:170px;top:2674px;list-style:none;font-size:12.5px;color:var(--text)}
.contact-list li{display:flex;align-items:center;gap:18px;height:36px}
.contact-list svg{width:14px;height:14px}
.social{left:170px;top:2800px;display:flex;gap:10px}
.social span{width:34px;height:34px;border-radius:50%;background:var(--accent)}
.field{left:632px;width:396px;border:1px solid var(--line);font-size:11px;color:var(--text);padding:10px 14px;border-radius:2px}
.contact .btn{left:632px;top:2824px;width:148px;height:40px}

/* footer */
.footer{left:0;top:2930px;width:1200px;height:65px;background:var(--footer);display:flex;align-items:center;justify-content:center;gap:18px;font-size:11px;color:#d6d8dc}
</style>
</head>
<body>

<header class="abs hero" role="img" aria-label="Dark photograph of a craftsman carving wood with a chisel">
  <div class="abs brand"><span class="dot"></span>Valqueno</div>
  <nav class="abs nav">
    <span>SERVICES</span><span>ABOUT US</span><span>CONTACT</span>
    <span class="lang"><span class="flag"></span>ENGLISH
      <svg width="8" height="6" viewBox="0 0 8 6"><path d="M1 1l3 3 3-3" stroke="#fff" fill="none" stroke-width="1.4"/></svg></span>
  </nav>
  <h1 class="abs hero-title">WOODWORKS</h1>
  <p class="abs hero-sub">Are you interested in an estimate?</p>
  <a class="abs btn">GET A QUOTE</a>
  <div class="abs dots"><span></span><span></span><span></span><span></span><span></span></div>
</header>

<svg width="0" height="0" style="position:absolute">
  <symbol id="tick" viewBox="0 0 11 9"><path d="M1 4.5l3 3L10 1" stroke="#1f9ae0" stroke-width="2" fill="none"/></symbol>
</svg>

<h2 class="abs section-title" style="top:618px">OUR SERVICES</h2>

<div class="photo" style="left:100px;top:710px;width:432px;height:300px;background:linear-gradient(135deg,#6b5a48,#a8875f 50%,#d4b98a)" role="img" aria-label="Wood carving with chisels and wood shavings on a workbench"></div>
<div class="abs service" style="left:596px;top:712px;width:480px">
  <h3>Woodworks</h3>
  <p>Timber is, in essence, a natural and warm material. Wood is also relatively durable and easy to work with, which has made it a favourite of builders throughout history. Our goal is to offer suitable products and quality furniture with installation and after-sales service to all of our clients. In order to achieve this, we're ready to help our clients in all stages of construction from design to production and maintenance.</p>
  <ul class="ticks">
    <li><svg><use href="#tick"/></svg>Furniture</li><li><svg><use href="#tick"/></svg>Staircases</li>
    <li><svg><use href="#tick"/></svg>Windows</li><li><svg><use href="#tick"/></svg>Woodcarving</li>
    <li><svg><use href="#tick"/></svg>Doors</li><li><svg><use href="#tick"/></svg>Graining</li>
  </ul>
</div>

<div class="abs service" style="left:124px;top:1090px;width:490px">
  <h3>Stoneworks</h3>
  <p>The natural stone found in the ground has been used in construction for centuries because of its durability. A structure built by a skilled craftsman from natural stone is unique, genuine and durable, and perfect for our bracing climate.<br>Our experienced craftsmen are ready to help you in all stages of construction from planning to completion.</p>
  <ul class="ticks">
    <li><svg><use href="#tick"/></svg>Walls</li><li><svg><use href="#tick"/></svg>Outdoor kitchens</li>
    <li><svg><use href="#tick"/></svg>Terraces</li><li><svg><use href="#tick"/></svg>Fireplaces/Smokeries</li>
    <li><svg><use href="#tick"/></svg>Paths</li><li><svg><use href="#tick"/></svg>Fences</li>
  </ul>
</div>
<div class="photo" style="left:668px;top:1088px;width:434px;height:300px;background:linear-gradient(135deg,#8a8e95,#5c6169 50%,#a59a8c)" role="img" aria-label="Hands laying paving stones with a hammer"></div>

<div class="photo" style="left:100px;top:1474px;width:432px;height:300px;background:linear-gradient(135deg,#e8e6e2,#b9a07a 55%,#6f8a5a)" role="img" aria-label="Restored wooden chairs and a round table by a window"></div>
<div class="abs service" style="left:596px;top:1476px;width:480px">
  <h3>Restoration</h3>
  <p>It's good to see that fixing old things has become popular again in recent years and people are trying to find ways to preserve valuable old windows and pieces of furniture before deciding to replace them.<br>It is possible to give a new life to almost any wooden door, window, piece of furniture or staircase. The extensive experience of our craftsmen will help you achieve the desired result.</p>
  <ul class="ticks">
    <li><svg><use href="#tick"/></svg>Furniture</li><li><svg><use href="#tick"/></svg>Staircases</li>
    <li><svg><use href="#tick"/></svg>Windows</li><li><svg><use href="#tick"/></svg>Floors</li>
    <li><svg><use href="#tick"/></svg>Doors</li><li><svg><use href="#tick"/></svg>Special Projects</li>
  </ul>
</div>

<section class="abs about" role="img" aria-label="Dim workshop background with woodworking tools">
  <h2 class="abs">ABOUT VALQUENO</h2>
  <div class="abs copy">
    <p>Valqueno is a company whose business operations include making wooden products, restoration and building structures from natural stone.</p>
    <p>All of our products are made by craftsmen and specialists who have extensive experience and knowledge in their fields.</p>
    <p>The products we offer are always handmade and we take the requests and ideas of the specific client into account. We always strive to achieve the best possible quality.</p>
    <p class="sign">Quality matters, Valqueno</p>
  </div>
  <div class="photo" style="left:614px;top:84px;width:488px;height:328px;background:linear-gradient(135deg,#6e4a2c,#a7754a 50%,#3d2a1d)" role="img" aria-label="Craftsman working at a wooden workbench"></div>
</section>

<section class="contact">
  <h2 class="abs section-title" style="top:2432px">CONTACT INFO</h2>
  <p class="abs contact-sub">WE'D LOVE TO HEAR FROM YOU SO WHY DON'T YOU GET IN TOUCH?</p>
  <div class="abs brand contact-brand"><span class="dot"></span>Valqueno</div>
  <ul class="abs contact-list">
    <li><svg viewBox="0 0 14 14"><path d="M7 1a4 4 0 0 0-4 4c0 3 4 8 4 8s4-5 4-8a4 4 0 0 0-4-4z" fill="#1f9ae0"/><circle cx="7" cy="5" r="1.5" fill="#fff"/></svg>Kase 12, 10115 Harbourton</li>
    <li><svg viewBox="0 0 14 14"><path d="M3 1l2.5 3-1.5 1.5c.8 1.8 2.2 3.2 4 4L9.5 8 13 10.5 11.5 13C6 13 1 8 1 2.5z" fill="#1f9ae0"/></svg>+000 55 01234</li>
    <li><svg viewBox="0 0 14 14"><rect x="1" y="3" width="12" height="8" fill="none" stroke="#1f9ae0" stroke-width="1.4"/><path d="M1 3l6 5 6-5" fill="none" stroke="#1f9ae0" stroke-width="1.4"/></svg>info@valqueno.example</li>
  </ul>
  <div class="abs social" aria-label="Social network links"><span></span><span></span><span></span><span></span><span></span></div>
  <div class="abs field" style="top:2562px;height:40px">Name :</div>
  <div class="abs field" style="top:2618px;height:40px">Email :</div>
  <div class="abs field" style="top:2674px;height:40px">Phone :</div>
  <div class="abs field" style="top:2730px;height:78px">Message :</div>
  <a class="abs btn">SEND</a>
</section>

<footer class="abs footer">
  <span>© 2016. Valqueno. All rights reserved.</span>
  <span>Contact</span><span>/</span><span>Terms &amp; Conditions</span><span>/</span><span>Privacy Policy</span>
</footer>

</body>
</html>
```